Business Card Design Project for Electrical Company

We need a business card designed for a new Electrical Company called Dorvel Electrical Solutions, i dont mind if only Dorvel Electrical is used. We are a domestic and commercial Electrical Company that provides a range of Electrical Services. Our Company colours are Fluro Yellow and Black with the Lightning bolt picture attached.I have attached a card that has been made i think it is rather basic and am looking for something more. the font of Dorvel Electrical has been used on our car graphics as well as the lightning bolt. i want to keep them the same so we can brand our business. Some things we want on the front of the card are Dorvel Electrical Solutions, Owen Platt, 0438516274, admin@dorvelelectrical.example, Lic No 58342, Servicing CQ Region. But we want Owens name seperate to the phone number as its the phone number for the office, owen wont be answering the phone so we are thinking we dont want to give that impression. What do you think? with all that if you have complete different font designs please submit what you think would work best. keeping in mind our company name and details as well as coulors.

Industry/Entity Type

Business

```html
<!DOCTYPE html>
<html lang="en">
<head>
<meta charset="utf-8">
<title>Dorvel Electrical Solutions – Business Card</title>
<link rel="stylesheet" href="https://fonts.googleapis.com/css2?family=Questrial&family=Montserrat:wght@700&display=swap">
<style>
  :root {
    --backdrop: #e8e8ec;
    --charcoal: #2a2a2a;
    --lime: #c9d61a;
    --paper: #f7f8fa;
    --ink-light: #e6e6e6;
    --ink-muted: #cfcfcf;
    --ink-dark: #2f2f2f;
  }
  * { box-sizing: border-box; margin: 0; padding: 0; }
  html, body { width: 1200px; height: 934px; overflow: hidden; }
  body {
    background: var(--backdrop);
    font-family: "Questrial", "Century Gothic", sans-serif;
    position: relative;
  }
  .card {
    position: absolute;
    top: 312px;
    width: 540px;
    height: 310px;
    overflow: hidden;
    box-shadow: 0 6px 18px rgba(0,0,0,0.12);
  }

  /* Lightning artwork area */
  .bolt-art { position: absolute; border-radius: 50%; }
  .card--services .bolt-art {
    left: 250px; top: -30px; width: 220px; height: 200px;
    background: radial-gradient(ellipse at center, rgba(255,255,255,0.16) 0%, rgba(255,255,255,0) 70%);
  }
  .card--contact .bolt-art {
    left: 210px; top: 10px; width: 200px; height: 170px;
    background: radial-gradient(ellipse at center, rgba(40,40,40,0.14) 0%, rgba(40,40,40,0) 70%);
  }

  /* Reverse side: services */
  .card--services { left: 40px; background: var(--charcoal); }
  .card--services .brand { position: absolute; right: 36px; top: 44px; }
  .card--services .brand-tagline { color: var(--ink-light); }
  .services { position: absolute; list-style: none; color: var(--ink-light); font-size: 19px; line-height: 31px; letter-spacing: 0.5px; }
  .services li::before { content: "•"; font-size: 12px; margin-right: 10px; vertical-align: 2px; }
  .services--primary { left: 38px; top: 66px; }
  .services--secondary { left: 300px; top: 159px; }
  .card--services .accent-band { position: absolute; left: 0; right: 0; bottom: 12px; height: 9px; background: var(--lime); }

  /* Front side: contact */
  .card--contact { left: 620px; background: var(--paper); }
  .card--contact .brand { position: absolute; right: 40px; top: 48px; }
  .card--contact .brand-tagline { color: var(--ink-dark); }
  .card--contact .accent-band { position: absolute; left: 0; right: 0; top: 166px; height: 12px; background: var(--lime); }
  .contact-panel { position: absolute; left: 0; right: 0; top: 178px; bottom: 0; background: var(--charcoal); }

  .brand { font-family: "Questrial", "Century Gothic", sans-serif; color: var(--lime); }
  .brand-name { font-size: 38px; line-height: 38px; letter-spacing: 1px; text-transform: uppercase; }
  .brand-tagline { font-size: 24px; line-height: 28px; letter-spacing: 2px; text-transform: uppercase; margin-left: 120px; }

  .person { position: absolute; left: 36px; bottom: 28px; color: var(--ink-light); }
  .person-name { font-family: "Montserrat", sans-serif; font-weight: 700; font-size: 17px; letter-spacing: 0.5px; text-transform: uppercase; }
  .person-role { font-size: 18px; margin-top: 4px; color: var(--ink-muted); }

  .contact-list { position: absolute; left: 270px; top: 16px; list-style: none; color: var(--ink-light); font-size: 14px; line-height: 22px; }
  .contact-list li { display: flex; align-items: center; gap: 10px; }
  .contact-list svg { width: 14px; height: 14px; flex: none; }

  .credentials { position: absolute; left: 270px; bottom: 28px; color: var(--ink-muted); font-size: 13px; line-height: 19px; }
  .credentials .licence { color: var(--lime); }
</style>
</head>
<body>

<section class="card card--services" aria-label="Card reverse: services">
  <div class="bolt-art" role="img" aria-label="Lightning bolt artwork behind the company name"></div>
  <div class="brand">
    <div class="brand-name">Dorvel<br>Electrical</div>
    <div class="brand-tagline">Solutions</div>
  </div>
  <ul class="services services--primary">
    <li>Light &amp; Power</li>
    <li>TV &amp; Data</li>
    <li>Test &amp; Tagging</li>
    <li>Residential</li>
    <li>Renovations</li>
    <li>Design &amp; Installation</li>
  </ul>
  <ul class="services services--secondary">
    <li>Air Con Installation</li>
    <li>Smoke Detectors</li>
  </ul>
  <div class="accent-band"></div>
</section>

<section class="card card--contact" aria-label="Card front: contact details">
  <div class="bolt-art" role="img" aria-label="Lightning bolt artwork behind the company name"></div>
  <div class="brand">
    <div class="brand-name">Dorvel<br>Electrical</div>
    <div class="brand-tagline">Solutions</div>
  </div>
  <div class="accent-band"></div>
  <div class="contact-panel">
    <ul class="contact-list">
      <li>
        <svg viewBox="0 0 14 14" aria-hidden="true"><rect x="3" y="0.8" width="8" height="12.4" rx="1.5" fill="none" stroke="#c9d61a" stroke-width="1.4"/><line x1="6" y1="11" x2="8" y2="11" stroke="#c9d61a" stroke-width="1.2"/></svg>
        0438 516 274
      </li>
      <li>
        <svg viewBox="0 0 14 14" aria-hidden="true"><rect x="0.5" y="2.5" width="13" height="9" fill="#c9d61a"/><polyline points="0.5,2.5 7,8 13.5,2.5" fill="none" stroke="#2a2a2a" stroke-width="1.2"/></svg>
        admin@dorvelelectrical.example
      </li>
    </ul>
    <div class="person">
      <div class="person-name">Owen Platt</div>
      <div class="person-role">Licensed Electrician</div>
    </div>
    <div class="credentials">
      <div class="licence">Lic No 58342</div>
      <div class="region">Servicing CQ Region</div>
    </div>
  </div>
</section>

</body>
</html>
```